Visitenkarten-Design für Forschungs- und Beratungsunternehmen
Zielgruppe
*Veridora' ist ein Forschungs- und Beratungsunternehmen für Lebensmittelwirkungen. Unsere Angebote sind: Vorträge, Workshops, Seminare und Coaching. Die Zielgruppen sind Pädagogen, Mediziner, Psychologen u.a.m.
Aufgabenstellung
Bei Bedarf kann die Gestaltung der Visitenkarte auch auf die Rückseite ausgedehnt werden.

```html
<!DOCTYPE html>
<html lang="de">
<head>
<meta charset="utf-8">
<title>Veridora – Visitenkarte</title>
<link href="https://fonts.googleapis.com/css2?family=Montserrat:wght@400;600;700&display=swap" rel="stylesheet">
<style>
  :root {
    --page-bg: #d9d9dc;
    --card-white: #ffffff;
    --card-black: #1f1f20;
    --ink: #222226;
    --ink-soft: #55555b;
    --divider: #9a9aa0;
    --brand: #e0208c;
    --purple: #6b2fa0;
    --magenta: #d81b8a;
    --orange: #f28a1a;
    --yellow: #f5d20f;
    --green: #7bc043;
    --blue: #1ea4e0;
    --navy: #1d2a4a;
  }
  * { box-sizing: border-box; margin: 0; padding: 0; }
  html, body {
    width: 1200px; height: 901px; overflow: hidden;
    background: var(--page-bg);
    font-family: "Montserrat", Arial, sans-serif;
  }
  .stage {
    width: 1200px; height: 901px;
    display: flex; align-items: center; justify-content: center; gap: 60px;
  }
  .card {
    position: relative; width: 520px; height: 297px; overflow: hidden;
    box-shadow: 0 10px 28px rgba(0,0,0,.25);
  }
  .card--front { background: var(--card-white); }
  .card--back { background: var(--card-black); display: flex; align-items: center; justify-content: center; }

  .brand {
    position: absolute; left: 48px; top: 112px; display: flex; align-items: center; gap: 10px;
  }
  .brand__dot { width: 18px; height: 18px; border-radius: 50%; background: var(--brand); }
  .brand__name { font-weight: 700; font-size: 30px; color: var(--brand); letter-spacing: .5px; }

  .divider { position: absolute; left: 250px; top: 58px; width: 1.5px; height: 120px; background: var(--divider); }

  .contact { position: absolute; left: 272px; top: 56px; color: var(--ink); }
  .contact__name { font-weight: 700; font-size: 17px; }
  .contact__role { font-size: 12px; color: var(--ink-soft); margin: 2px 0 10px; }
  .contact__list { list-style: none; font-size: 12.5px; line-height: 1.55; }
  .contact__list li { display: flex; align-items: center; gap: 7px; }
  .contact__list svg { width: 12px; height: 12px; fill: var(--ink); flex: none; }

  .spectrum-strip {
    position: absolute; right: 0; top: 190px; width: 250px; height: 10px;
    background: linear-gradient(90deg, var(--green), var(--yellow), var(--orange), var(--magenta), var(--blue));
  }
  .address-band {
    position: absolute; left: 120px; right: 0; bottom: 36px; height: 26px;
    background: linear-gradient(90deg, var(--purple), var(--magenta) 25%, var(--orange) 50%, var(--yellow) 62%, var(--blue) 82%, var(--navy));
    display: flex; align-items: center; gap: 6px; padding-left: 14px;
    color: #fff; font-size: 12px; font-weight: 600;
  }
  .address-band svg { width: 11px; height: 11px; fill: #fff; }
  .corner-block { position: absolute; left: 0; bottom: 0; width: 120px; height: 16px; background: var(--green); }

  .back-brand { display: flex; align-items: center; gap: 14px; }
  .back-brand__dot { width: 26px; height: 26px; border-radius: 50%; background: var(--brand); }
  .back-brand__name { font-weight: 700; font-size: 44px; color: var(--brand); letter-spacing: 1px; }
</style>
</head>
<body>
<main class="stage">
  <section class="card card--front" aria-label="Vorderseite">
    <div class="brand"><span class="brand__dot"></span><span class="brand__name">Veridora</span></div>
    <div class="divider"></div>
    <div class="contact">
      <p class="contact__name">Lukas Brenner</p>
      <p class="contact__role">Director</p>
      <ul class="contact__list">
        <li><svg viewBox="0 0 24 24"><path d="M6.6 10.8a15 15 0 0 0 6.6 6.6l2.2-2.2c.3-.3.7-.4 1-.2 1.1.4 2.3.6 3.6.6.6 0 1 .4 1 1V20c0 .6-.4 1-1 1A17 17 0 0 1 3 4c0-.6.4-1 1-1h3.5c.6 0 1 .4 1 1 0 1.3.2 2.5.6 3.6.1.3 0 .7-.2 1z"/></svg>+41 61 555 24 90</li>
        <li><svg viewBox="0 0 24 24"><path d="M2 5h20v14H2zm2 2v.5l8 5 8-5V7z"/></svg>info@veridora.ch</li>
        <li><svg viewBox="0 0 24 24"><circle cx="12" cy="12" r="10"/></svg>www.veridora.ch</li>
        <li><svg viewBox="0 0 24 24"><path d="M12 2a7 7 0 0 0-7 7c0 5 7 13 7 13s7-8 7-13a7 7 0 0 0-7-7zm0 9.5A2.5 2.5 0 1 1 12 6a2.5 2.5 0 0 1 0 5.5z"/></svg>CH-4410 Talwil</li>
      </ul>
    </div>
    <div class="spectrum-strip"></div>
    <div class="address-band">
      <svg viewBox="0 0 24 24"><path d="M12 2a7 7 0 0 0-7 7c0 5 7 13 7 13s7-8 7-13a7 7 0 0 0-7-7zm0 9.5A2.5 2.5 0 1 1 12 6a2.5 2.5 0 0 1 0 5.5z"/></svg>
      1200 Sample Road, Kenton AK 99000
    </div>
    <div class="corner-block"></div>
  </section>

  <section class="card card--back" aria-label="Rückseite">
    <div class="back-brand"><span class="back-brand__dot"></span><span class="back-brand__name">Veridora</span></div>
  </section>
</main>
</body>
</html>
```